Flyer
Zielgruppe
Wir vertreiben Handwerkskunst aus fernen Länder: Indonesien, China, Indien, Nepal, Marokko, Türkei, Thailand, Mexiko.
Zielgruppe ist jeder, der offen für fremde Kulturen, besondere und nachhaltige Einrichtung ist.
Aufgabenstellung
Ich benötige zum 1. Geburtstag unseres besonderen Einrichtungshauses ein Layout, welches ich als Flyer, aber auch als A1 Plakat nutzen kann. Bei den Plakaten ist zu beachten, dass diese an Straßenlaternen auf Höhe Unterkante 2,50 gehängt werden. Also wenige plakative Informationen, die man beim vorbeifahren aufnehmen kann. Max. 1 Foto aus den Beispielen im Anhang. Hintergrund Orange, wie auf den Eröffnungsplakaten. Schrittypen der Beispiele bitte übernehmen.
Hier die Infos - Texte können angepasst werden:
1 Jahre huber's SPEICHERHOF in Bayreuth
Freitag, 01.09. & Samstag 02.09.23
Wir feiern sagen Danke mit tollen Angeboten und Aktionen:
15% auf ein Möbelstück Ihrer Wahl
30€ kaufen - 20€ zahlen
Gratis Möbellieferung
1 Flasche türkischen Wein im wert von 7,80€ bei jedem Einkauf ab 10€ Gratis (Bild ist beigefügt)
Angebote gültig bis 30.09.23
huber's Speicherhof
Tannwalder Weg 14
95448 Bayreuth
im Gebäude vom Technik Moser

```html
<!DOCTYPE html>
<html lang="de">
<head>
<meta charset="utf-8">
<title>huber's Speicherhof – 1 Jahre in Bayreuth</title>
<link href="https://fonts.googleapis.com/css2?family=Poppins:wght@400;600;700&family=Oswald:wght@500;600&display=swap" rel="stylesheet">
<style>
  :root {
    --stage: #a0682a;
    --paper: #ffffff;
    --orange: #e0892a;
    --red: #c9252c;
    --ink: #3a3a3a;
    --dark: #1f1915;
  }
  html, body { margin: 0; padding: 0; overflow: hidden; }
  body { width: 1200px; height: 1200px; background: var(--stage); position: relative; }
  .flyer {
    position: absolute; left: 20px; top: 190px;
    width: 1218px; height: 860px;
    transform: scale(0.9524); transform-origin: top left;
    background: var(--paper); overflow: hidden;
    font-family: 'Poppins', sans-serif; color: var(--ink);
  }
  .shapes { position: absolute; inset: 0; }
  .abs { position: absolute; }
  .brand { left: 24px; top: 62px; width: 420px; text-align: center; }
  .brand-name { font-size: 31px; font-weight: 600; letter-spacing: 2px; color: var(--ink); line-height: 1.2; white-space: nowrap; }
  .brand-tag { font-family: 'Oswald', sans-serif; font-weight: 500; font-size: 15px; color: var(--ink); margin-top: 10px; white-space: nowrap; }
  .headline {
    left: 34px; top: 180px; width: 400px; text-align: center;
    font-size: 44px; font-weight: 700; line-height: 1.12; color: var(--orange); margin: 0;
  }
  .dates {
    left: 84px; top: 310px; width: 310px; padding: 12px 0;
    background: var(--red); color: #fff; transform: rotate(-12deg);
    font-size: 22px; font-weight: 600; line-height: 1.2; text-align: center;
  }
  .intro { left: 72px; top: 418px; font-size: 21px; line-height: 1.25; margin: 0; }
  .offer-percent {
    left: 20px; top: 482px; width: 220px; text-align: right;
    font-size: 26px; font-weight: 700; line-height: 1.16; color: var(--red);
  }
  .offer-divider { left: 268px; top: 488px; width: 2px; height: 86px; background: var(--orange); }
  .offer-buy {
    left: 287px; top: 486px; font-family: 'Oswald', sans-serif; font-weight: 600;
    font-size: 34px; line-height: 1.2; color: var(--orange); white-space: nowrap;
  }
  .wine-badge {
    left: 437px; top: 468px; width: 310px; height: 310px; border-radius: 50%;
    background: var(--orange); color: #fff; text-align: center;
    display: flex; flex-direction: column; justify-content: center; align-items: center;
  }
  .wine-badge .small { font-size: 19px; line-height: 1.35; margin-bottom: 8px; }
  .wine-badge .big { font-size: 29px; font-weight: 700; line-height: 1.24; }
  .delivery {
    left: 841px; top: 474px; width: 200px; text-align: center;
    color: #fff; font-weight: 600; font-size: 17px; line-height: 1.45;
  }
  .address { left: 740px; top: 662px; width: 474px; text-align: center; font-size: 21px; line-height: 1.35; }
  .web { left: 740px; top: 736px; width: 474px; text-align: center; font-size: 21px; color: var(--orange); }
  .countries {
    left: 548px; top: 795px; width: 664px; height: 65px; line-height: 65px;
    text-align: center; color: #fff; font-family: 'Oswald', sans-serif; font-weight: 500;
    font-size: 20px; letter-spacing: -0.2px; white-space: nowrap;
  }
</style>
</head>
<body>
  <div class="flyer">
    <svg class="shapes" width="1218" height="860" viewBox="0 0 1218 860">
      <defs>
        <linearGradient id="wood" x1="0" y1="0" x2="1" y2="1">
          <stop offset="0" stop-color="#3b2a1f"/><stop offset="1" stop-color="#1e1713"/>
        </linearGradient>
        <linearGradient id="warm" x1="0" y1="0" x2="1" y2="1">
          <stop offset="0" stop-color="#6b5340"/><stop offset="1" stop-color="#2e241c"/>
        </linearGradient>
        <linearGradient id="blue" x1="0" y1="0" x2="0" y2="1">
          <stop offset="0" stop-color="#8a96a8"/><stop offset="1" stop-color="#2c3748"/>
        </linearGradient>
        <linearGradient id="dresser" x1="0" y1="0" x2="0" y2="1">
          <stop offset="0" stop-color="#c8c6c0"/><stop offset="0.55" stop-color="#5f7fae"/><stop offset="1" stop-color="#4a5b73"/>
        </linearGradient>
      </defs>

      <path class="orange-field" d="M634,0 H1218 V522 Q1040,565 820,480 Q680,300 634,0 Z" fill="var(--orange)"/>

      <g class="photo-grid">
        <rect x="495" y="38" width="244" height="217" fill="url(#wood)" role="img" aria-label="Foto: bemalter niedriger Holztisch mit Teetassen"/>
        <rect x="749" y="38" width="275" height="217" fill="url(#blue)" role="img" aria-label="Foto: blau-weiß bemalte Keramikdosen"/>
        <rect x="1033" y="38" width="145" height="217" fill="#2a3a4a" role="img" aria-label="Foto: blau lackierter Schrank mit Blumenmotiv"/>
        <rect x="495" y="263" width="147" height="217" fill="#d9d2c6" role="img" aria-label="Foto: goldene Buddha-Wanddekoration"/>
        <rect x="652" y="263" width="350" height="217" fill="url(#dresser)" role="img" aria-label="Foto: blaue Vintage-Kommode mit grünen Glasflaschen"/>
        <rect x="1012" y="263" width="166" height="217" fill="#a69682" role="img" aria-label="Foto: gemusterte Bodenkissen"/>
      </g>

      <path class="wine-photo" d="M0,605 Q180,570 330,600 Q470,640 560,860 H0 Z" fill="url(#warm)" role="img" aria-label="Foto: türkische Weinflaschen in einer Holzkiste"/>

      <path class="country-band" d="M535,795 H1218 V860 H555 Q548,825 535,795 Z" fill="var(--red)"/>

      <polygon class="delivery-star" fill="var(--red)"
        points="941,340 972,425 1093,373 1015,460 1101,528 1001,532 1031,655 956,565 941,655 915,568 847,627 872,540 792,525 872,478 798,420 905,430"/>
    </svg>

    <div class="abs brand">
      <div class="brand-name">huber's SPEICHERHOF</div>
      <div class="brand-tag">handgefertigte Waren und ausgefallene Wohnkultur</div>
    </div>

    <h1 class="abs headline">1 JAHRE<br>IN BAYREUTH</h1>

    <div class="abs dates">Freitag, 01.09. &amp;<br>Samstag 02.09.23</div>

    <p class="abs intro">Wir feiern sagen Danke mit tollen<br>Angeboten und Aktionen:</p>

    <div class="abs offer-percent">15%AUF EIN<br>MÖBELSTÜCK<br>IHRER WAHL</div>
    <div class="abs offer-divider"></div>
    <div class="abs offer-buy">30€ KAUFEN<br>20€ ZAHLEN</div>

    <div class="abs wine-badge">
      <div class="small">1 Flasche türkischen<br>Wein im wert</div>
      <div class="big">von 7,80€ bei<br>jedem Einkauf ab<br>10€ Gratis</div>
    </div>

    <div class="abs delivery">GRATIS<br>MÖBELLIEFERUNG</div>

    <div class="abs address">Tannwalder Weg 14 · 95448 Bayreuth ·<br>Im Gebäude von Technik Moser</div>
    <div class="abs web">www.hubers-speicherhof.de</div>

    <div class="abs countries">CHINA · INDONESIEN · THAILAND · INDIEN · MAROKKO · NEPAL · TÜRKEI · MEXIKO</div>
  </div>
</body>
</html>
```